KORVEL Flyer

We need a flyer for the research project called 'KORVEL'. We will distribute this flyer during conferences and events to our audience (mainly industry (Security and IoT), medical organisations, and researchers) in order to provide the basic information about the project.
The project will provide a Holistic Network Guard Framework for the Health-Care Industry.
We are attaching files to provide with concrete information on our requirements:
- KORVEL brochure content_final.ppt: includes the content we would like to include in the flyer. There is also the URL to the project website
- KORVEL layout.doc: it includes information about the layout (example video from another project brochure)
- KORVEL logo final version_sourcefile.zip: the project logo
- Logo-partners.zip: Logos that will be included (please follow the numbered order.)
We would like to use colors that belong to the project logo color range. Regarding the images that you may include in the brochure we wouldn't like to propose any because we do not want to limitate your imagination. They could be relevant to medical devices, security, etc.

```html
<!DOCTYPE html>
<html lang="en">
<head>
<meta charset="utf-8">
<title>KORVEL Flyer</title>
<link rel="stylesheet" href="https://fonts.googleapis.com/css2?family=Comfortaa:wght@500;600&family=Oswald:wght@500&family=Roboto:wght@400&display=swap">
<style>
  :root {
    --teal: #17a093;
    --teal-deep: #0f9187;
    --band: #232323;
    --ink-soft: #5c5c5c;
    --rule: #d7e6e4;
    --paper: #ffffff;
  }
  * { margin: 0; padding: 0; box-sizing: border-box; }
  html, body { width: 872px; height: 1200px; overflow: hidden; background: var(--paper); }
  .flyer { position: relative; width: 872px; height: 1200px; overflow: hidden; background: var(--paper); }
  .shapes { position: absolute; inset: 0; width: 872px; height: 1200px; }
  .topics {
    position: absolute; right: 36px; top: 44px; text-align: right;
    font-family: "Comfortaa", sans-serif; font-weight: 600; color: var(--teal);
    font-size: 19px; line-height: 29px; list-style: none;
  }
  .title-band {
    position: absolute; left: 0; top: 571px; width: 872px; height: 72px;
    background: var(--band); display: flex; align-items: center; justify-content: center;
  }
  .title {
    font-family: "Oswald", sans-serif; font-weight: 500; color: #fff;
    font-size: 38px; letter-spacing: 0.3px; text-transform: uppercase;
  }
  .subtitle {
    position: absolute; left: 0; width: 872px; top: 652px; text-align: center;
    font-family: "Oswald", sans-serif; font-weight: 500; color: #fff;
    font-size: 31px; letter-spacing: 0.3px; text-transform: uppercase;
  }
  .brand {
    position: absolute; left: 60px; top: 952px; display: flex; align-items: center; gap: 18px;
  }
  .brand-dot { width: 64px; height: 64px; border-radius: 50%; border: 7px solid var(--teal); }
  .brand-name {
    font-family: "Comfortaa", sans-serif; font-weight: 500; color: var(--teal);
    font-size: 48px; letter-spacing: 1px;
  }
  .footer-rule { position: absolute; left: 0; top: 1076px; width: 872px; height: 2px; background: var(--rule); }
  .contacts {
    position: absolute; top: 1112px; left: 0; width: 872px;
    font-family: "Roboto", sans-serif; font-size: 15px; color: var(--ink-soft); line-height: 24px;
  }
  .contacts .col { position: absolute; top: 0; white-space: nowrap; }
  .col-social { left: 60px; }
  .col-network { left: 346px; }
  .col-web { left: 620px; }
</style>
</head>
<body>
<main class="flyer">
  <svg class="shapes" viewBox="0 0 727 1000">
    <defs>
      <linearGradient id="lower-diamond" x1="0" y1="0" x2="1" y2="1">
        <stop offset="0" stop-color="#1fab9f"/>
        <stop offset="1" stop-color="#0e8d83"/>
      </linearGradient>
      <linearGradient id="photo-fill" x1="0" y1="0" x2="1" y2="1">
        <stop offset="0" stop-color="#cfe3e2"/>
        <stop offset="0.45" stop-color="#3f9f95"/>
        <stop offset="1" stop-color="#2a8a80"/>
      </linearGradient>
    </defs>
    <polygon class="diamond-lower" points="305,290 620,605 390,835 75,520" fill="url(#lower-diamond)"/>
    <polygon class="diamond-frame" points="348,15 597,262 348,510 100,262" fill="var(--teal-deep)"/>
    <polygon class="diamond-photo" role="img" aria-label="Photo of surgeons in scrubs working under operating-room lights"
             points="348,50 562,262 348,475 134,262" fill="url(#photo-fill)"/>
  </svg>

  <ul class="topics">
    <li>Cybersecurity Vulnerability</li>
    <li>Assessment &amp; Certification</li>
    <li>Medical &amp; health Devices</li>
    <li>Healthcare Services</li>
    <li>Cybersecurity</li>
    <li>Data Privacy</li>
  </ul>

  <div class="title-band"><h1 class="title">A Holistic Network Guard Framework</h1></div>
  <p class="subtitle">For the Health-Care Industry</p>

  <div class="brand">
    <span class="brand-dot"></span>
    <span class="brand-name">KORVEL</span>
  </div>

  <div class="footer-rule"></div>
  <footer class="contacts">
    <div class="col col-social">Chirpa: @ProjectKorvel<br>Circlebook Page: korvel-project.eu</div>
    <div class="col col-network">ProNet Page: korvel-project<br>ClipStream: The korvel project eu</div>
    <div class="col col-web">Web: https://korvel-project.eu/</div>
  </footer>
</main>
</body>
</html>
```